Virtual Personal Training Flyer Design

We are a virtual personal training website, acting as the intermediary between the customer and the personal trainer. The customer can choose their personal trainer based on specialty and then subscribe and have access to their videos, training nutritional advice and live sessions.
We have sent over an orange and blue background for inspiration of the theme and also our three logos. Brightpeak Fitness is the company and BrightpeakLDX is the product and the F is our standard logo.
We want our social media links on the flyer which are Twitter: @BrightpeakLDX and Facebook: BrightpeakLDX. We also want our e-mail address which is brightpeakldx@quillmail.net and telephone number which is 07518269352.

We also want to put the key benefits for consumers onto the flyers, which are wide variety of personal trainers to choose from and tailored to you, have constant access to videos etc, save time travelling to the gym, saving effort - more convenient, cheaper than personal training in the gym - saving money, gain from trainer's knowledge - more informed about workout and what exercises you are doing etc. We would like to add rhetorical questions such as Want a personal trainer but can't afford one? or Want to have a structured training program but haven't got the time or access to a gym?
We also want our slogan on there which is LDX, become the you, you've always wanted to be.

Target Market(s)

women aged between 18 and 35

Industry/Entity Type

Personal Trainer

Requirements
Should not have
• don't want old fonts or clash colours and shouldn't be cartooney.

```html
<!DOCTYPE html>
<html lang="en">
<head>
<meta charset="utf-8">
<title>Brightpeak Fitness – Virtual Personal Training Flyer</title>
<link href="https://fonts.googleapis.com/css2?family=League+Gothic&family=Oswald:wght@400;500&family=Roboto+Condensed:wght@300;400&display=swap" rel="stylesheet">
<style>
  :root {
    --backdrop: #5e6168;
    --orange-light: #ec8a2e;
    --orange: #d7680f;
    --orange-deep: #a94f0c;
    --headline: #e4e4e4;
    --band-blue: #2b87c5;
    --brand-blue: #1f5fae;
    --brand-orange: #f08a1c;
    --contact-blue: #2a6fb4;
    --paper: #ffffff;
    --paper-shade: #e9e9e9;
    --device-light: #eeeeee;
    --device-dark: #bdbdbd;
  }
  * { margin: 0; padding: 0; box-sizing: border-box; }
  html, body { width: 1200px; height: 1000px; overflow: hidden; }
  body { background: var(--backdrop); position: relative; font-family: "Oswald", sans-serif; }

  .flyer {
    position: absolute; left: 270px; top: 30px; width: 658px; height: 925px;
    background: var(--paper); overflow: hidden;
  }
  .hero {
    position: absolute; left: 0; top: 0; width: 100%; height: 668px;
    background: radial-gradient(ellipse at 70% 30%, var(--orange-light) 0%, var(--orange) 45%, var(--orange-deep) 100%);
  }
  .device-showcase {
    position: absolute; left: 70px; top: 127px; width: 505px; height: 345px;
    border-radius: 10px;
    background: linear-gradient(160deg, var(--device-light) 0%, var(--device-dark) 100%);
    opacity: 0.9;
  }
  .headline {
    position: absolute; left: 0; width: 100%; color: var(--headline); text-align: center;
    font-family: "League Gothic", "Oswald", sans-serif; font-weight: 400; line-height: 1;
  }
  .headline-kicker { top: 497px; font-size: 36px; letter-spacing: 0.5px; padding-left: 52px; }
  .headline-main { top: 527px; font-size: 88px; letter-spacing: 0; }
  .headline-tag {
    position: absolute; top: 602px; right: 110px; color: var(--headline);
    font-family: "Roboto Condensed", sans-serif; font-size: 14px; font-weight: 400;
  }

  .benefit-band {
    position: absolute; left: 0; top: 668px; width: 100%; height: 54px;
    background: var(--band-blue); color: #fff; text-align: center;
    font-family: "Roboto Condensed", sans-serif;
  }
  .benefit-intro { font-weight: 300; font-size: 19px; line-height: 25px; padding-top: 2px; }
  .benefit-list { font-weight: 400; font-size: 19.5px; line-height: 24px; }

  .footer {
    position: absolute; left: 0; top: 722px; width: 100%; height: 203px;
    background: linear-gradient(180deg, var(--paper-shade) 0%, var(--paper) 40%, var(--paper) 70%, var(--paper-shade) 100%);
  }
  .brand {
    position: absolute; top: 40px; left: 0; width: 100%;
    display: flex; justify-content: center; align-items: center; gap: 16px;
  }
  .brand-name { color: var(--brand-orange); font-weight: 500; font-size: 50px; line-height: 1; }
  .brand-mark { width: 36px; height: 36px; background: var(--brand-blue); }

  .contacts {
    position: absolute; top: 148px; left: 46px; right: 46px;
    display: flex; justify-content: space-between; align-items: center;
    font-family: "Roboto Condensed", sans-serif; font-size: 14px; color: var(--contact-blue);
  }
  .contact { display: flex; align-items: center; gap: 5px; white-space: nowrap; }
  .contact svg { fill: var(--contact-blue); }
  .contact-dot { width: 10px; height: 10px; border-radius: 50%; background: var(--contact-blue); }
</style>
</head>
<body>
  <main class="flyer">
    <section class="hero">
      <div class="device-showcase" role="img" aria-label="Desktop monitor, tablet and phone displaying the BrightpeakLDX website with the line 'Connecting you to the right personal trainer' and a row of exercise silhouettes"></div>
      <h1>
        <span class="headline headline-kicker">VIRTUAL</span>
        <span class="headline headline-main">PERSONAL TRAINING</span>
      </h1>
      <span class="headline-tag">WEBSITE</span>
    </section>

    <section class="benefit-band">
      <p class="benefit-intro">Choose your trainer and get instant access to</p>
      <p class="benefit-list">VIDEOS • TRAINING • NUTRITIONAL ADVICE • LIVE SESSIONS</p>
    </section>

    <footer class="footer">
      <div class="brand">
        <span class="brand-name">Brightpeak Fitness</span>
        <span class="brand-mark" aria-hidden="true"></span>
      </div>
      <div class="contacts">
        <span class="contact">
          <svg width="11" height="15" viewBox="0 0 11 15" aria-hidden="true"><path d="M3 0 L5 3.5 L3.5 5 Q4 9 7 11 L8.5 9.5 L11 12 L9 14.5 Q1 13 0.5 3 Z"/></svg>
          0 (751) 826-9352
        </span>
        <span class="contact">
          <svg width="19" height="13" viewBox="0 0 19 13" aria-hidden="true"><rect x="0" y="0" width="19" height="13"/><path d="M0.5 0.5 L9.5 7.5 L18.5 0.5" fill="none" stroke="#fff" stroke-width="1.4"/></svg>
          brightpeakldx@quillmail.net
        </span>
        <span class="contact"><span class="contact-dot" aria-hidden="true"></span>@BrightpeakLDX</span>
        <span class="contact"><span class="contact-dot" aria-hidden="true"></span>BrightpeakLDX</span>
      </div>
    </footer>
  </main>
</body>
</html>
```